Marketing Brochure - Conjunction event

We need a brochure for clients/conjunction real estate agents to view the type of projects VARO531 have available.
As a guideline of our requirements, please refer to our company profile. As you can see it is a simple elegant professional image we are after.
We are a Real Estate company specialise in off the plans project marketing. We have sale teams to sell the projects/ residential properties but also conjunction with other real estate agents. This is the first time we decided to use QuillMarket to design our brochure. If pleasing results, ongoing we will have many more design projects to do.

Target Market(s)

Clients / real estate agents

Industry/Entity Type

Real Estate

Font styles to use
Sans Serif

Colors
ffffff
ef484e

Requirements
Must have
• All the details in the documents, Encourage creative designs.
• Company logo and the black banner as seen on company profile brochure
Nice to have
• similar to our company profile brochure( file attached)
Should not have
• Funky or too loud type image

```html
<!DOCTYPE html>
<html lang="en">
<head>
<meta charset="utf-8">
<title>Project Brochure</title>
<link rel="stylesheet" href="https://fonts.googleapis.com/css2?family=Raleway:ital,wght@0,400;0,500;0,600;0,700;0,800;1,500&display=swap">
<style>
:root{
  --backdrop:#9b9b9b;
  --paper:#ffffff;
  --banner:#2b2624;
  --accent:#ef484e;
  --ink:#1a1a1a;
  --rule:#111111;
}
*{box-sizing:border-box;margin:0;padding:0}
html,body{width:1200px;height:841px;overflow:hidden}
body{background:var(--backdrop);font-family:"Raleway",sans-serif;color:var(--ink);position:relative}
.page{position:absolute;top:23px;width:558px;height:789px;background:var(--paper)}
.page--left{left:25px}
.page--right{left:602px}
.banner{height:152px;background:var(--banner);text-align:center;color:#fff;padding-top:86px}
.banner__title{font-size:33px;font-weight:800;line-height:1;letter-spacing:.2px}
.banner__place{font-size:19px;font-style:italic;font-weight:500;line-height:1.2;margin-top:2px}
.status{text-align:center;color:var(--accent);font-weight:800;font-size:19px;margin-top:4px}
.address{position:absolute;left:90px;top:215px;width:378px;height:22px;border-bottom:2px solid var(--rule)}
.address__tag{position:absolute;left:0;bottom:0;height:20px;width:70px;background:var(--accent);color:#fff;font-weight:700;font-size:12px;line-height:20px;padding-left:8px;clip-path:polygon(0 0,88% 0,100% 100%,0 100%)}
.address__text{position:absolute;right:0;bottom:2px;text-align:right;font-size:8.5px;line-height:1.25}
.photo{position:absolute;top:240px;height:120px}
.photo--small{left:90px;width:150px}
.photo--large{left:255px;width:213px}
.photo--dusk{background:linear-gradient(180deg,#6b5a6e 0%,#b98a6e 45%,#7c6454 100%)}
.photo--sky{background:linear-gradient(180deg,#9fb8d6 0%,#c7ccce 50%,#6f6a62 100%)}
.photo--garden{background:linear-gradient(180deg,#c89a6a 0%,#8a6a7e 45%,#4e5a32 100%)}
.photo--lawn{background:linear-gradient(180deg,#b9c9d6 0%,#a8a6a0 45%,#4f7a3a 100%)}
.facts{position:absolute;left:90px;width:150px;font-size:9px;line-height:1.3}
.fact{border-top:2px solid var(--rule);padding-top:8px;height:41px}
.fact__value{color:var(--accent);font-weight:600}
.features{position:absolute;left:255px;width:213px;font-size:9px;line-height:1.35}
.features__head{color:var(--accent);font-weight:600;border-bottom:2px solid var(--rule);padding-bottom:2px;margin-bottom:5px}
.features__list{list-style:none;text-align:justify}
.features__list li::before{content:"\2022 ";color:var(--accent)}
.deposit{border-top:2px solid var(--rule);padding-top:8px;margin-top:6px}
.deposit__value{color:var(--accent);font-weight:600}
.units{position:absolute;left:90px;width:380px;border-collapse:collapse;font-size:8.5px;text-align:center}
.units th,.units td{border:2px solid var(--rule)}
.units th{color:var(--accent);font-weight:600;height:54px;line-height:1.3;vertical-align:middle}
.units td{height:17px}
</style>
</head>
<body>

<section class="page page--left">
  <header class="banner">
    <h1 class="banner__title">The Harbourline</h1>
    <p class="banner__place">-Arncliffe Sydney-</p>
  </header>
  <p class="status">SOLD OUT !</p>

  <div class="address">
    <span class="address__tag">Address</span>
    <span class="address__text">210 Harbour Road,<br>Arncliffe NSW 2205</span>
  </div>
  <div class="photo photo--small photo--dusk" role="img" aria-label="Evening render of the apartment building on the street corner"></div>
  <div class="photo photo--large photo--sky" role="img" aria-label="Daytime render of the apartment building facade"></div>

  <div class="facts" style="top:380px">
    <div class="fact">Developer<br><span class="fact__value">Kestrel Group</span></div>
    <div class="fact">Architect<br><span class="fact__value">Halden Ross</span></div>
    <div class="fact">Builder<br><span class="fact__value">Kestrel Construction</span></div>
    <div class="fact">Estimated Completion<br><span class="fact__value">End of 2017</span></div>
    <div class="fact">Building Attributes<br><span class="fact__value">Apartments over 6 levels<br>Ground Floor retail and restaurant</span></div>
  </div>

  <div class="features" style="top:367px">
    <p class="features__head">Feature Include</p>
    <ul class="features__list">
      <li>Mix of spacious 1 &amp; 2bedroom apartments</li>
      <li>Just 10km South of Sydney CBD</li>
      <li>Only 3 min to Arncliffe train station</li>
      <li>6 min drive to Sydney airport</li>
      <li>5 min walk to the local public school</li>
      <li>Close to Arncliffe village and major shopping centre</li>
      <li>Stroll along the promenade beside the water in Brighton-Le-Sands</li>
      <li>Close to the proposed Sydney next Business Technology Park – Cooks Cove,</li>
      <li>Easy access to M5</li>
    </ul>
    <div class="deposit">Deposit Requirement<br><span class="deposit__value">10% deposit (Cash Deposit, Bank Guarantee)</span></div>
  </div>

  <table class="units" style="top:604px">
    <colgroup><col style="width:40px"><col style="width:46px"><col style="width:62px"><col style="width:75px"><col style="width:72px"><col></colgroup>
    <tr><th>Apt.<br>Type</th><th>No.<br>Available</th><th>Internal Size<br>(sqm)</th><th>Price Range<br>From high</th><th>Rental estimate<br>Per week</th><th>Annual Strata<br>Levies</th></tr>
    <tr><td>Studio</td><td>1</td><td>50-55</td><td>-</td><td>$440</td><td>$500 - $600</td></tr>
    <tr><td>1 Bed</td><td>35</td><td>72-105</td><td>$564K - $567K</td><td>$480 - $550</td><td>$600 - $800</td></tr>
    <tr><td>2 Bed</td><td>148</td><td>45</td><td>$687K - $768K</td><td>$580 - $700</td><td>$700 - $900</td></tr>
    <tr><td>3 Bed</td><td>3</td><td>110</td><td>$687K</td><td>$750- $800</td><td>$1000+</td></tr>
  </table>
</section>

<section class="page page--right">
  <header class="banner">
    <h1 class="banner__title">Belwood Estate</h1>
    <p class="banner__place">-Ryde Sydney-</p>
  </header>
  <p class="status">Stage III - Released</p>

  <div class="address">
    <span class="address__tag">Address</span>
    <span class="address__text">58 Linden Street,<br>Ryde NSW 2114</span>
  </div>
  <div class="photo photo--small photo--garden" role="img" aria-label="Dusk render of the estate buildings behind flowering trees"></div>
  <div class="photo photo--large photo--lawn" role="img" aria-label="Render of the estate courtyard lawn with a blossoming tree"></div>

  <div class="facts" style="top:380px">
    <div class="fact">Developer<br><span class="fact__value">Kestrel Group</span></div>
    <div class="fact">Architect<br><span class="fact__value">Halden Ross</span></div>
    <div class="fact">Builder<br><span class="fact__value">Kestrel Construction</span></div>
    <div class="fact" style="padding-top:4px">Building Attributes<br><span class="fact__value">416 Apartments over 6 levels<br>Ground Floor retail and restaurant</span></div>
    <div class="fact" style="margin-top:8px;padding-top:6px;height:auto">Estimated completion <span class="fact__value">Early 2017</span><br>Council rates per annum $960<br>Water rates $700</div>
  </div>

  <div class="features" style="top:367px">
    <p class="features__head">Feature Include</p>
    <ul class="features__list">
      <li>Mix of spacious 1&amp; 2 bedroom apartments</li>
      <li>A village plaza - 26 speciality stores including FreshMart</li>
      <li>Only 20min to Sydney CBD</li>
      <li>Train : only 9 stops to Wynward Station (38 min)</li>
      <li>Ferry :13 stops from Meadowbank to Darling Harbour (50 min)</li>
      <li>Buses: Sydney buses run two routes via Meadowbank station.</li>
      <li>School – Meadowbank TAFE, Meadowbank public school, Ryde public school, West Ryde public school</li>
      <li>Situated just 5km from Sydney Olympic park and Macquarie University</li>
    </ul>
    <div class="deposit">Deposit Requirement<br><span class="deposit__value">10% deposit (Cash Deposit, Bank Guarantee)</span></div>
  </div>

  <table class="units" style="top:604px">
    <colgroup><col style="width:65px"><col style="width:40px"><col style="width:37px"><col style="width:70px"><col style="width:65px"><col></colgroup>
    <tr><th>Apt. Type</th><th>No.<br>Available</th><th>Internal<br>Size<br>(sqm)</th><th>Price Range<br>From high</th><th>Rental<br>estimate<br>Per week</th><th>Annual Strata<br>Levies</th></tr>
    <tr><td>1 Bed</td><td>25</td><td>52-66</td><td>$555K - $653K</td><td>$500 - $520</td><td>$550 - $570 per qtr</td></tr>
    <tr><td>1 Bed + Study</td><td>4</td><td>54-68</td><td>$610K - $669K</td><td>$550 - $600</td><td>$560 - $750</td></tr>
    <tr><td>2 Bed</td><td>7</td><td>82-83</td><td>$763K- $825K</td><td>$620 - $680</td><td>$750 - $1100</td></tr>
    <tr><td>3 Bed</td><td>3</td><td>103</td><td>$935K - $955K</td><td>$700- $750</td><td>$900 - $1200</td></tr>
  </table>
</section>

</body>
</html>
```